Overseas Property Tax Depreciation

We need a two sided flyer to promote our business and explain what we do. our website is www.tolvexhq.net.
The attached word file is what I would like on an A5 size flyer with one side showing the FAQ and the other the worked example. I would like these formatted much better than the are and in general style of the website. I will attach files for logos as well.

Business

```html
<!DOCTYPE html>
<html lang="en">
<head>
<meta charset="utf-8">
<title>Tolvex Tax Depreciation – Flyer</title>
<link href="https://fonts.googleapis.com/css2?family=Didact+Gothic&family=Arimo:wght@400;700&display=swap" rel="stylesheet">
<style>
:root{
  --stage:#8f8f8f;
  --paper:#ffffff;
  --cream:#fbe9cf;
  --green:#5aa81e;
  --green-dark:#3f8a12;
  --green-light:#8cc63f;
  --orange:#f7a21b;
  --yellow:#ffd21c;
  --ink:#333333;
  --rule:#8a8a8a;
}
*{box-sizing:border-box;margin:0;padding:0}
html,body{width:1200px;height:1000px;overflow:hidden}
body{background:var(--stage);font-family:"Arimo",Arial,sans-serif;color:var(--ink);position:relative}

.flyer{position:absolute;background:linear-gradient(180deg,var(--paper) 0%,var(--paper) 45%,var(--cream) 100%);overflow:hidden}
.flyer__glow{position:absolute;border-radius:50%;background:radial-gradient(circle,rgba(255,214,120,0) 35%,rgba(255,214,120,.35) 45%,rgba(255,214,120,0) 60%)}
.flyer__band{position:absolute;left:0;right:0;bottom:0;background:linear-gradient(90deg,var(--green-light),var(--green));z-index:1}
.brand{position:absolute;display:flex;align-items:center;gap:6px;font-family:"Didact Gothic",sans-serif;color:#fff;font-size:17px;white-space:nowrap;z-index:3}
.brand__dot{width:12px;height:12px;border-radius:50%;background:var(--yellow)}

/* Front: worked example */
.front{left:115px;top:45px;width:645px;height:465px}
.front__title{position:absolute;left:34px;top:20px;font-family:"Didact Gothic",sans-serif;font-size:14.5px;color:var(--green);white-space:nowrap}
.example{position:absolute;left:45px;top:50px;width:565px;border-collapse:collapse;font-size:8px;background:rgba(255,255,255,.75);box-shadow:4px 4px 4px rgba(0,0,0,.25)}
.example td,.example th{font-weight:400;padding:1px 4px;height:14.3px;text-align:left;border-left:1px solid var(--rule);white-space:nowrap}
.example col.c-ref{width:35px}.example col.c-desc{width:313px}.example col.c-eur{width:59px}.example col.c-aud{width:60px}.example col.c-rep{width:98px}
.example tbody{border-top:4px solid var(--rule)}
.example tbody:first-of-type{border-top:none}
.example .eur,.example .aud{background:linear-gradient(90deg,var(--yellow),var(--orange))}
.example .rep{background:linear-gradient(90deg,var(--green-light),var(--green))}
.example .head th{height:20px;text-align:center;font-size:7px;vertical-align:bottom}
.example .pad td{height:8px}
.example .muted td{color:#6aa84f}
.example .muted .rep{color:#b8df8e}
.example .line td{border-top:1px solid var(--rule)}
.note{display:inline-block;width:120px}
.note--wide{width:190px}

/* Back: FAQ */
.back{left:487px;top:520px;width:648px;height:465px}
.faq{position:absolute;z-index:2;background:rgba(255,255,255,.72);padding:5px 8px 6px;font-size:6.4px;line-height:1.3;box-shadow:2px 2px 5px rgba(0,0,0,.18)}
.faq__q{font-family:"Didact Gothic",sans-serif;color:var(--green);font-size:14px;line-height:1.05;text-align:center;margin-bottom:3px}
.faq p{margin-bottom:1px}
.faq--why{left:14px;top:30px;width:440px;transform:rotate(2deg)}
.faq--ireland{left:462px;top:12px;width:168px;transform:rotate(-2deg)}
.faq--what{left:8px;top:232px;width:285px;transform:rotate(-4deg)}
.faq--missed{left:302px;top:206px;width:185px;transform:rotate(-3deg)}
.faq--cost{left:100px;top:330px;width:210px;transform:rotate(-4deg)}
.faq--old{left:412px;top:305px;width:215px;transform:rotate(-6deg)}
.seal{position:absolute;right:10px;top:10px;width:22px;height:22px;border-radius:50%;background:#fff;border:2px solid #e3c21c}
.member-mark{position:absolute;left:12px;bottom:9px;width:60px;height:24px;border:2px solid #fff;border-radius:3px;z-index:3}
</style>
</head>
<body>

<section class="flyer front" aria-label="Worked example side">
  <div class="flyer__glow" style="left:250px;top:-120px;width:520px;height:520px"></div>
  <h1 class="front__title">Property Tax Depreciation Example 3 bed Semi - detached house Dublin, Constructed in 2006</h1>
  <table class="example">
    <colgroup><col class="c-ref"><col class="c-desc"><col class="c-eur"><col class="c-aud"><col class="c-rep"></colgroup>
    <tbody>
      <tr class="head"><th>Ref</th><th style="text-align:left">Description</th><th class="eur" colspan="2">Without Property<br>Tax Depreciation</th><th class="rep">With Property<br>Depreciation Report</th></tr>
      <tr><td></td><td></td><td class="eur" style="text-align:center">Euro</td><td class="aud" style="text-align:center">AUD</td><td class="rep" style="text-align:center">AUD</td></tr>
    </tbody>
    <tbody>
      <tr class="pad"><td></td><td></td><td class="eur"></td><td class="aud"></td><td class="rep"></td></tr>
      <tr><td>A</td><td><span class="note note--wide">Rental Income</span>€1,200&nbsp;&nbsp;&nbsp;&nbsp;&nbsp;&nbsp;&nbsp;&nbsp;Month</td><td class="eur">€14,400</td><td class="aud">$20,571</td><td class="rep">$20,571</td></tr>
      <tr class="pad"><td></td><td></td><td class="eur"></td><td class="aud"></td><td class="rep"></td></tr>
    </tbody>
    <tbody>
      <tr><td></td><td>Expenses</td><td class="eur"></td><td class="aud"></td><td class="rep"></td></tr>
      <tr><td>B</td><td>Annual Interest charged on<br>outstanding Mortgage (4% apr)</td><td class="eur">€12,040</td><td class="aud">$17,200</td><td class="rep">$17,200</td></tr>
      <tr><td>C</td><td>Property agent fees or commission</td><td class="eur">€1,200</td><td class="aud">$1,714</td><td class="rep">$1,714</td></tr>
      <tr><td>D</td><td>Local Property Tax</td><td class="eur">€250</td><td class="aud">$357</td><td class="rep">$357</td></tr>
      <tr><td>E</td><td>Repairs and Maintenance</td><td class="eur">€2,000</td><td class="aud">$2,857</td><td class="rep">$2,857</td></tr>
      <tr><td>F</td><td>Home Insurance</td><td class="eur">€450</td><td class="aud">$643</td><td class="rep">$643</td></tr>
      <tr><td>G</td><td>Cleaning Advertising et..</td><td class="eur">€1,500</td><td class="aud">$2,143</td><td class="rep">$2,143</td></tr>
      <tr class="muted"><td>H</td><td>Property Tax Depreciation</td><td class="eur">€0</td><td class="aud">$0</td><td class="rep">$15,000</td></tr>
      <tr class="line"><td>I</td><td><span class="note">Total Annual&nbsp;&nbsp;&nbsp;&nbsp;&nbsp;&nbsp;Expenses</span>&nbsp;&nbsp;&nbsp;&nbsp;&nbsp;&nbsp;&nbsp;&nbsp;&nbsp;&nbsp;&nbsp;&nbsp;&nbsp;&nbsp;&nbsp;&nbsp;&nbsp;&nbsp;&nbsp;&nbsp;&nbsp;&nbsp;&nbsp;&nbsp;Total (B to H)</td><td class="eur">€17,440</td><td class="aud">$24,914</td><td class="rep">$39,914</td></tr>
      <tr class="line"><td>J</td><td><span class="note note--wide">Annual Rental Loss/Gain</span>(A less I)</td><td class="eur">€3,040</td><td class="aud">$4,343</td><td class="rep">$19,343</td></tr>
    </tbody>
    <tbody>
      <tr><td>K</td><td>Your Annual Income from other sources</td><td class="eur"></td><td class="aud">$180,000</td><td class="rep">$180,000</td></tr>
      <tr><td>L</td><td><span class="note note--wide">Tour Taxable Income after Rental Losses/Gains</span>(K Plus J)</td><td class="eur"></td><td class="aud">$175,657</td><td class="rep">$160,657</td></tr>
    </tbody>
    <tbody>
      <tr><td>N</td><td><span class="note note--wide">Annual Tax Saving&nbsp;&nbsp;Foreign Tax Credits</span>(J multiplied by M)</td><td class="eur"></td><td class="aud">$1,694</td><td class="rep">$7,544</td></tr>
      <tr><td>O</td><td><span class="note note--wide">Non-resident Landlord withholding Tax (20% Ireland)</span>(A multiplied by 20%)</td><td class="eur">€2,880</td><td class="aud">$4,114</td><td class="rep">$4,114</td></tr>
      <tr><td>P</td><td><span class="note note--wide">Nett Tax Savings</span>(N Plus O)</td><td class="eur"></td><td class="aud">$5,808</td><td class="rep">$11,658</td></tr>
      <tr class="pad"><td></td><td></td><td class="eur"></td><td class="aud"></td><td class="rep"></td></tr>
    </tbody>
    <tbody>
      <tr class="pad"><td></td><td></td><td class="eur"></td><td class="aud"></td><td class="rep"></td></tr>
      <tr><td>Q</td><td>Additional Money in your Pocket (Australia)<br>per year due to Property Tax Depreciation</td><td class="eur"></td><td class="aud"></td><td class="rep">$5,850</td></tr>
      <tr class="pad"><td></td><td></td><td class="eur"></td><td class="aud"></td><td class="rep"></td></tr>
    </tbody>
  </table>
  <div class="flyer__band" style="height:50px"></div>
  <div class="brand" style="right:30px;bottom:11px"><span class="brand__dot"></span>Tolvex Tax Depreciation</div>
</section>

<section class="flyer back" aria-label="Frequently asked questions side">
  <div class="flyer__glow" style="left:-90px;top:-150px;width:500px;height:500px"></div>
  <div class="seal" aria-label="Registered agent badge" role="img"></div>

  <article class="faq faq--why">
    <h2 class="faq__q">Why use us?</h2>
    <p>There are several websites out there offering tax depreciation reports for Australian properties but there are very few who are appropriately qualified and approved by the Australian Tax Office (ATO) and offer the necessary Irish expertise. The Quantity Surveyor that prepares your report:</p>
    <p>Is Irish and qualified as a Quantity Surveyor in Ireland.</p>
    <p>Worked there during the "Celtic Tiger" period when construction costs were quite high.</p>
    <p>Has detailed knowledge of Irish construction methods and costs over the past 20 years. Irish buildings are generally much more expensive than Australia due to the climate, just think about how many Australian houses you have seen that have double glazing, central heating, insulation etc..</p>
    <p>Has a partnership arrangement with an Irish quantity surveying firm to carry out the property inspections required in most cases to maximize the deductions available.</p>
    <p>Is a chartered member of the Chartered Surveyors Guild.</p>
    <p>Maintains the Appropriate Professional Indemnity Insurance.</p>
    <p>Is registered with the Tax Agents Registry. All quantity surveyors who prepare Property Tax Depreciation Schedules are required by the ATO to be registered with the Tax Agents Registry which checks that the person preparing the reports is suitably qualified and maintains the appropriate professional indemnity insurance. You can check the registration on the TAR website. Our registration number is 31807264.</p>
  </article>

  <article class="faq faq--ireland">
    <h2 class="faq__q">My property<br>is in Ireland does<br>this make<br>a difference?</h2>
    <p>Division 43 of the Income Tax Assessment Act 1997 which deals with capital works depreciation states that it applies to buildings begun outside Australia after 21 August 1990 Sect 43.20 (1) (b). Your Australian tax return should cover your worldwide income. As long as the property is available to rent back in Ireland you are obliged by the ATO to report any income or loss on that property.</p>
  </article>

  <article class="faq faq--what">
    <h2 class="faq__q">What is Property Depreciation?</h2>
    <p>Just like you claim wear and tear on a car purchased for income producing purposes, you can also claim the depreciation of your investment property against your taxable income.</p>
    <p>There are 2 types available: depreciation on Plant and Equipment, and depreciation on the cost of construction. Plant and Equipment refers to items within the building like ovens, dishwashers, carpet and blinds etc. Both these costs can be offset against your assessable income.</p>
  </article>

  <article class="faq faq--missed">
    <h2 class="faq__q">I haven't included my property for the past couple of years on my tax return is this a problem?</h2>
    <p>No, in actual fact you could have been missing out on savings for a number of years, you can also use this report to claim a refund from the ATO for up to the past three years.</p>
  </article>

  <article class="faq faq--cost">
    <h2 class="faq__q">How much will<br>the report cost?</h2>
    <p>Each scenario is different so contact us to obtain a quick quote for your situation. Generally the cost of the report is a fraction of the savings in any one year.</p>
    <p>Our fee is fully tax deductible.</p>
    <p>You do NOT need to get this report done every year so the cost can be spread over several years.</p>
  </article>

  <article class="faq faq--old">
    <h2 class="faq__q">Is my property<br>too old?</h2>
    <p>No, if your property was constructed after 1990 you can claim for both the construction cost element and the Plant and equipment. If it was built before then you can still claim the plant and equipment allowance. The easiest thing to do is to contact us with some details on your property and we can make an initial assessment of the possible annual savings.</p>
  </article>

  <div class="flyer__band" style="height:44px"></div>
  <div class="member-mark" role="img" aria-label="Professional membership badge"></div>
  <div class="brand" style="right:22px;bottom:9px"><span class="brand__dot"></span>Tolvex Tax Depreciation</div>
</section>

</body>
</html>
```